BRISKEL , FOLD LANTERN APA

Hey,

I would like to get a beer label that looks like Pemberly Guitar combo with master volume knob to show% ABV beer, beer Gain knob to show the style of APA and the Clean button to display the Best Data before. logo tag on the top of the briskel, under the middle part of Fold Lantern. lable overall dimensions are 162 millimeters wide and 90 millimeters high, the image should fit within the central part of the label area of ​​90x90 millimeters.
Attached files are easy to see my idea of label drawing , also can see my last beer label design (designed by Dale Wruton by my sketch)- a similar style I would like for the new label too.
Feel free to also create yours vision of this idea, it does not have to be exactly like my sketch. Briskel logo letters could be as in the wayward IPA label. The text could be a font of Antenna Black

Target Market(s)

craft beer drinkers, bars, pubs, beer shops etc

```html
<!DOCTYPE html>
<html lang="en">
<head>
<meta charset="utf-8">
<title>Briskel – Fold Lantern APA label</title>
<link rel="stylesheet" href="https://fonts.googleapis.com/css2?family=Montserrat:wght@700;800;900&display=swap">
<style>
  :root {
    --paper: #ffffff;
    --ink: #000000;
    --panel: #2a2a2a;
    --grille: #1c1c1c;
    --gold: #efcf8a;
    --white: #ffffff;
  }
  html, body {
    margin: 0;
    padding: 0;
    width: 1200px;
    height: 1000px;
    overflow: hidden;
    background: var(--paper);
  }
  .label {
    display: block;
    width: 1200px;
    height: 1000px;
  }
  .cabinet-area { fill: var(--ink); }
  .grille-area { fill: var(--grille); }
  .panel { fill: var(--panel); }
  .ink-fill { fill: var(--ink); }
  .gold-fill { fill: var(--gold); }
  .white-fill { fill: var(--white); }
  .tagline {
    font-family: "Montserrat", sans-serif;
    font-weight: 800;
    font-size: 22px;
    fill: var(--gold);
  }
  .brand-name {
    font-family: "Montserrat", sans-serif;
    font-weight: 900;
    font-size: 128px;
    fill: var(--ink);
  }
  .beer-name {
    font-family: "Montserrat", sans-serif;
    font-weight: 700;
    font-size: 84px;
    fill: var(--white);
    stroke: var(--ink);
    stroke-width: 12px;
    stroke-linejoin: round;
    paint-order: stroke;
    letter-spacing: 4px;
  }
  .knob-text {
    font-family: "Montserrat", sans-serif;
    font-weight: 800;
    font-size: 22px;
    fill: var(--ink);
  }
  .brewed-text {
    font-family: "Montserrat", sans-serif;
    font-weight: 800;
    font-size: 22px;
    fill: var(--gold);
  }
  .knob-pointer {
    stroke: var(--ink);
    stroke-width: 8px;
  }
</style>
</head>
<body>
<svg class="label" viewBox="0 0 1200 1000" xmlns="http://www.w3.org/2000/svg">
  <!-- cabinet illustration area -->
  <rect class="cabinet-area" x="135" y="37" width="927" height="925" role="img" aria-label="Guitar amplifier cabinet illustration with handles, side rails and screws"/>

  <!-- top panel with tagline -->
  <rect class="panel" x="250" y="80" width="698" height="77"/>
  <text class="tagline" x="600" y="137" text-anchor="middle" textLength="626" lengthAdjust="spacingAndGlyphs">Handcrafted unfiltered hopy beer for beerbrothers</text>

  <!-- brand band -->
  <rect class="gold-fill" x="250" y="157" width="698" height="138"/>
  <text class="brand-name" x="600" y="274" text-anchor="middle" textLength="622" lengthAdjust="spacingAndGlyphs">BRISKEL</text>

  <!-- speaker grille area -->
  <rect class="grille-area" x="250" y="297" width="698" height="553" role="img" aria-label="Speaker grille cloth pattern"/>

  <!-- speaker badge -->
  <circle class="ink-fill" cx="597" cy="572" r="235"/>
  <circle class="panel" cx="597" cy="572" r="225"/>
  <text class="beer-name" x="597" y="510" text-anchor="middle">FOLD</text>
  <text class="beer-name" x="597" y="605" text-anchor="middle" textLength="390" lengthAdjust="spacingAndGlyphs">LANTERN</text>
  <text class="beer-name" x="597" y="700" text-anchor="middle">APA</text>

  <!-- volume knob: ABV -->
  <circle class="ink-fill" cx="342" cy="766" r="64"/>
  <circle class="gold-fill" cx="342" cy="766" r="53"/>
  <line class="knob-pointer" x1="345" y1="755" x2="372" y2="722"/>
  <text class="knob-text" x="342" y="784" text-anchor="middle">6.66%</text>
  <text class="knob-text" x="342" y="808" text-anchor="middle">ABV</text>

  <!-- gain knob: IBU -->
  <circle class="ink-fill" cx="862" cy="762" r="64"/>
  <circle class="gold-fill" cx="862" cy="762" r="53"/>
  <line class="knob-pointer" x1="858" y1="751" x2="831" y2="720"/>
  <text class="knob-text" x="862" y="795" text-anchor="middle">50 IBU</text>

  <!-- bottom panel with brew date -->
  <rect class="panel" x="250" y="858" width="698" height="72"/>
  <rect class="ink-fill" x="415" y="870" width="363" height="40"/>
  <text class="brewed-text" x="430" y="899">BREWED</text>
  <rect class="white-fill" x="553" y="880" width="212" height="21"/>
</svg>
</body>
</html>
```